Medical IT Business with New logo needs a fresh stationary design

First time on pixel Harbor; Thought I would give it a go.
This project is for business cards alone but we have loads of design work that needs to take place in the immediate future.

We provide IT services to the Medical Industry and value ourselves as offering a premium product to the market.

I am after a fresh, clean design using full colour 2 sided cards which includes our current colour palettes from our logo.

Card's must include:
- Logo
- Slogan
- Name
- Adress
- Email
- Phone
- Fax
- Mobile

Target Market(s)

Surgeons, High Profile Medical Personnel

Industry/Entity Type

Business

Fonts, CMYK Colours and Logo files attached.

Requirements
Must have
• Card's must include:
• - Logo
• - Slogan
• - Name
• - Adress
• - Email
• - Phone
• - Fax
• - Mobile
Nice to have
• Needs to incorporate our colour palette (attached CMYK colours)
Should not have
• Black backgrounds. Black text ok.

```html
<!DOCTYPE html>
<html lang="en">
<head>
<meta charset="utf-8">
<title>Clinara Networks – Business Card</title>
<link href="https://fonts.googleapis.com/css2?family=Source+Sans+3:wght@400;700&display=swap" rel="stylesheet">
<style>
  :root {
    --frame-yellow: #ffd800;
    --paper: #ffffff;
    --brand-blue: #057db5;
    --navy: #14325a;
    --slogan-grey: #a9a8c2;
    --on-navy: #ffffff;
  }
  * { margin: 0; padding: 0; box-sizing: border-box; }
  html, body { width: 1200px; height: 1200px; overflow: hidden; }
  body {
    font-family: "Source Sans 3", "Myriad Pro", sans-serif;
    background: var(--frame-yellow);
    position: relative;
  }
  .sheet {
    position: absolute;
    left: 19px; top: 24px;
    width: 1162px; height: 1157px;
    background: var(--paper);
  }
  .abs { position: absolute; line-height: 1; white-space: nowrap; }

  /* Front card */
  .card-front {
    position: absolute;
    left: 94px; top: 62px;
    width: 800px; height: 536px;
    background: var(--brand-blue);
  }
  .card-front .inner {
    position: absolute;
    left: 12px; top: 12px;
    width: 776px; height: 512px;
    background: var(--navy);
  }
  .card-front .content {
    position: absolute;
    left: 5px; top: 4px;
    width: 767px; height: 441px;
    background: var(--paper);
  }
  .brand-dot {
    position: absolute;
    left: 146px; top: 144px;
    width: 173px; height: 173px;
    border-radius: 50%;
    background: var(--brand-blue);
  }
  .brand-name { color: var(--navy); font-weight: 700; letter-spacing: -1px; }
  .brand-name.line-1 { left: 384px; top: 160px; font-size: 88px; }
  .brand-name.line-2 { left: 542px; top: 232px; font-size: 61px; }
  .slogan { left: 384px; top: 292px; font-size: 34px; color: var(--slogan-grey); }
  .holder-name { left: 424px; top: 366px; font-size: 66px; color: var(--navy); }
  .mobile { left: 452px; top: 466px; font-size: 31px; color: var(--brand-blue); }
  .address { left: 113px; top: 538px; font-size: 30px; color: var(--on-navy); }

  /* Back card */
  .card-back {
    position: absolute;
    left: 306px; top: 599px;
    width: 800px; height: 535px;
    background: var(--navy);
  }
  .contact { color: var(--on-navy); font-size: 32px; left: 360px; }
  .contact.mail { top: 87px; }
  .contact.phone { top: 212px; }
  .contact.fax { top: 346px; }

  .side-label { color: var(--navy); font-size: 61px; }
  .side-label.front { left: 910px; top: 226px; }
  .side-label.back { left: 86px; top: 794px; }
</style>
</head>
<body>
  <main>
    <div class="sheet"></div>

    <section class="card-front" aria-label="Card front">
      <div class="inner"><div class="content"></div></div>
    </section>
    <div class="brand-dot" aria-hidden="true"></div>
    <div class="abs brand-name line-1">CLINARA</div>
    <div class="abs brand-name line-2">NETWORKS</div>
    <div class="abs slogan">care connected, every day</div>
    <div class="abs holder-name">NAME</div>
    <div class="abs mobile">moblie</div>
    <div class="abs address">Address:</div>

    <div class="abs side-label front">front</div>

    <section class="card-back" aria-label="Card back">
      <div class="abs contact mail">MAIL</div>
      <div class="abs contact phone">PHONE</div>
      <div class="abs contact fax">FAX</div>
    </section>

    <div class="abs side-label back">back</div>
  </main>
</body>
</html>
```